Cosmetics Store Website

High end cosmetics/skincare store needs a new website. We are a locally owned company based in Idaho. We have an initial site map and some copy and we are looking for someone who can not only DESIGN but get a full website UP AND RUNNING! This will not be a shopping cart style site (we do not sell online) but rather an information site about our locations, our brands, our services, our mission, job opportunities etc. We would like to see a mock up of our home page and hear how you plan to code/set up the rest of our site. We would prefer to keep the company name confidential, but know that our logo is black and just a stylized lettering of our company name.
More details like company name, logo, pictures, etc can be given after we select a candidate.
Thank you!

```html
<!DOCTYPE html>
<html lang="en">
<head>
<meta charset="utf-8">
<title>Alpine Beauty</title>
<link href="https://fonts.googleapis.com/css2?family=Roboto:wght@100;300;400;500&display=swap" rel="stylesheet">
<style>
  :root {
    --teal: #52cbbd;
    --teal-deep: #49c0b2;
    --teal-line: #5fd2c5;
    --white: #ffffff;
    --ink: #333333;
    --nav-ink: #555555;
  }
  * { margin: 0; padding: 0; box-sizing: border-box; }
  html, body {
    width: 1200px;
    height: 640px;
    overflow: hidden;
    background: var(--teal);
    font-family: "Roboto", Arial, sans-serif;
  }
  .page {
    position: relative;
    width: 1200px;
    height: 640px;
    overflow: hidden;
  }
  .site-header {
    position: absolute;
    top: 0; left: 0;
    width: 1200px;
    height: 62px;
    background: var(--white);
  }
  .brand {
    position: absolute;
    left: 33px;
    top: 18px;
    font-size: 19px;
    font-weight: 400;
    letter-spacing: 0.5px;
    color: var(--ink);
  }
  .main-nav {
    position: absolute;
    left: 243px;
    top: 21px;
    display: flex;
    gap: 32px;
    font-size: 15px;
    font-weight: 300;
    color: var(--nav-ink);
  }
  .search-icon {
    position: absolute;
    right: 25px;
    top: 19px;
  }
  .side-tools {
    position: absolute;
    top: 62px;
    right: 0;
    width: 56px;
  }
  .side-tools .tool {
    height: 56px;
    background: var(--teal-deep);
    border-bottom: 1px solid var(--teal-line);
    display: flex;
    align-items: center;
    justify-content: center;
    color: var(--white);
    font-size: 18px;
    font-weight: 300;
  }
  .side-tools .tool:first-child { height: 34px; align-items: flex-start; padding-top: 4px; }
  .side-tools .tool small { font-size: 10px; margin-left: 3px; margin-top: 4px; }
  .hero {
    position: absolute;
    top: 62px;
    left: 0;
    width: 1200px;
    height: 578px;
    text-align: center;
    color: var(--white);
  }
  .hero-title {
    position: absolute;
    top: 209px;
    left: 0;
    width: 1200px;
    font-size: 136px;
    font-weight: 100;
    line-height: 1;
    letter-spacing: 2px;
  }
  .hero-lead {
    position: absolute;
    top: 392px;
    left: 20px;
    width: 1160px;
    font-size: 20px;
    font-weight: 300;
    line-height: 29px;
    text-transform: uppercase;
  }
  .hero-actions {
    position: absolute;
    top: 524px;
    left: 381px;
    display: flex;
    gap: 8px;
  }
  .hero-button {
    width: 213px;
    height: 66px;
    border: 1px solid var(--white);
    display: flex;
    align-items: center;
    justify-content: center;
    font-size: 15px;
    font-weight: 500;
    color: var(--white);
    padding-bottom: 6px;
  }
</style>
</head>
<body>
<div class="page">
  <header class="site-header">
    <div class="brand">ALPINE BEAUTY</div>
    <nav class="main-nav">
      <span>About</span>
      <span>Contact</span>
      <span>Books-Videos</span>
      <span>Product</span>
    </nav>
    <svg class="search-icon" width="22" height="22" viewBox="0 0 22 22" aria-label="Search">
      <circle cx="9" cy="9" r="6.5" fill="none" stroke="#333" stroke-width="3"/>
      <line x1="14" y1="14" x2="20" y2="20" stroke="#333" stroke-width="3.4" stroke-linecap="round"/>
    </svg>
  </header>

  <main class="hero">
    <h1 class="hero-title">ALPINE BEAUTY</h1>
    <p class="hero-lead">We would prefer to keep the company name confidential, but know that our logo is black and just a stylized lettering of our company name. More details like company name, logo, pictures, etc can be given after we select a candidate.</p>
    <div class="hero-actions">
      <div class="hero-button">LOCATE US</div>
      <div class="hero-button">POPULAR PRODUCTS</div>
    </div>
  </main>

  <aside class="side-tools">
    <div class="tool">
      <svg width="20" height="16" viewBox="0 0 20 16" aria-label="Email">
        <rect x="1.5" y="1.5" width="17" height="13" rx="1.5" fill="none" stroke="#fff" stroke-width="2"/>
        <polyline points="2,3 10,9 18,3" fill="none" stroke="#fff" stroke-width="2"/>
      </svg>
    </div>
    <div class="tool">1<small>%</small></div>
    <div class="tool">
      <svg width="18" height="12" viewBox="0 0 18 12" aria-label="Scroll down">
        <polyline points="2,2 9,9 16,2" fill="none" stroke="#fff" stroke-width="3.4" stroke-linecap="round" stroke-linejoin="round"/>
      </svg>
    </div>
  </aside>
</div>
</body>
</html>
```